Business Card Trio Design

We need a set of business cards that all match but are not identical. We need one generic for the business and one for each of the two owners. We would like the cards to be similar to each other, but not identical. We have a logo and the colors of the logo are painstakingly chosen so if blue or green is used, we prefer our specific blue and green. Our logo pops better on a black background as well. We are open to double-sided, but it is not the top choice. We would love some either gold or silver accents that are in a foiled appearance. We sell uniforms (scrubs, culinary, EMT, police, fire, business, all types except kids and sports), shoes, equipment, and accessories. We also have quorvalink, mavelgrid, lumopixel, and yondrel that we would like to have them follow and we offer zembrix in the store we would like the card to also advertise.

```html
<!DOCTYPE html>
<html lang="en">
<head>
<meta charset="utf-8">
<title>Corvane Uniforms – Business Card</title>
<link rel="stylesheet" href="https://fonts.googleapis.com/css2?family=Montserrat:wght@400;500;700&display=swap">
<style>
  :root {
    --backdrop: #3a3431;
    --card: #1d1e20;
    --card-back: #161718;
    --brand-green: #14a37f;
    --brand-blue: #8fb0cc;
    --ink: #e9ecee;
    --silver-hi: #8a8c90;
    --silver-mid: #4a4b4f;
    --silver-lo: #1c1d1f;
  }
  * { margin: 0; padding: 0; box-sizing: border-box; }
  html, body { width: 1200px; height: 786px; overflow: hidden; }
  body {
    background: var(--backdrop);
    font-family: "Montserrat", Arial, sans-serif;
    position: relative;
  }

  .card {
    position: absolute;
    width: 540px;
    height: 309px;
    border-radius: 4px;
    box-shadow: 0 14px 30px rgba(0,0,0,.45);
    overflow: hidden;
  }
  .card--front { left: 40px; top: 420px; background: var(--card); }
  .card--back  { left: 620px; top: 60px; background: var(--card-back); }

  /* front */
  .front-decor {
    position: absolute; left: 240px; top: 10px;
    width: 190px; height: 170px;
    border-radius: 50%;
    background: radial-gradient(circle at 45% 40%, #2b2c2f 0%, #242527 55%, var(--card) 72%);
  }
  .brand {
    position: absolute; left: 36px; top: 40px;
    display: flex; align-items: center; gap: 12px;
  }
  .brand__dot {
    width: 40px; height: 40px; border-radius: 50%;
    background: var(--brand-green);
    flex: none;
  }
  .brand__name {
    color: var(--brand-blue);
    font-weight: 700; font-size: 19px; letter-spacing: 2px;
    line-height: 1.15; text-transform: uppercase;
  }

  .person__name {
    position: absolute; left: 36px; top: 148px;
    color: var(--brand-green); font-weight: 700; font-size: 23px; line-height: 28px;
  }
  .rule {
    position: absolute; left: 36px; right: 36px; top: 181px;
    height: 2px; background: var(--brand-green);
  }
  .person__role {
    position: absolute; left: 36px; top: 189px;
    color: var(--ink); font-size: 12px; line-height: 15px;
  }

  .contact {
    position: absolute; left: 36px; top: 214px;
    list-style: none; color: var(--ink); font-size: 13px;
  }
  .contact li { display: flex; align-items: center; gap: 10px; line-height: 20px; }
  .contact svg { width: 11px; height: 11px; flex: none; }
  .icon-fill { fill: var(--brand-green); }
  .icon-line { fill: none; stroke: var(--brand-green); stroke-width: 1.4; }

  .location {
    position: absolute; left: 366px; top: 124px;
    font-size: 12px; color: var(--ink); line-height: 17px;
  }
  .location__company { color: var(--brand-green); font-size: 13.5px; }

  /* back */
  .back-pattern {
    position: absolute; inset: 0;
    background: linear-gradient(100deg, var(--silver-hi) 0%, var(--silver-mid) 38%, #2a2b2d 68%, var(--silver-lo) 100%);
    opacity: .6;
  }
  .back-mark {
    position: absolute; right: 62px; top: 96px;
    width: 36px; height: 36px; border-radius: 50%;
    background: var(--brand-green);
  }
</style>
</head>
<body>

<section class="card card--front" aria-label="Business card front">
  <div class="front-decor" role="img" aria-label="Large faint brand symbol embossed in the card"></div>

  <div class="brand">
    <span class="brand__dot"></span>
    <span class="brand__name">Corvane<br>Uniforms</span>
  </div>

  <div class="person__name">Dorian Halvik</div>
  <div class="rule"></div>
  <div class="person__role">Owner</div>

  <ul class="contact">
    <li><svg viewBox="0 0 12 12"><path class="icon-fill" d="M2 1h3l1 3-1.5 1a7 7 0 0 0 2.5 2.5L8 6l3 1v3c0 .6-.4 1-1 1A10 10 0 0 1 1 2c0-.6.4-1 1-1z"/></svg>(555) 014-2231</li>
    <li><svg viewBox="0 0 12 12"><path class="icon-fill" d="M2 1h3l1 3-1.5 1a7 7 0 0 0 2.5 2.5L8 6l3 1v3c0 .6-.4 1-1 1A10 10 0 0 1 1 2c0-.6.4-1 1-1z"/></svg>(555) 018-4407</li>
    <li><svg viewBox="0 0 12 12"><path class="icon-line" d="M.7 2.5h10.6v7H.7z M.7 2.5l5.3 4 5.3-4"/></svg>corvaneuniformshop@mailbox.com</li>
    <li><svg viewBox="0 0 12 12"><circle class="icon-fill" cx="6" cy="6" r="5.5"/></svg>www.corvaneuniforms.com</li>
  </ul>

  <div class="location">
    <div class="location__company">Corvane Uniforms</div>
    <div>418 Brindle Plaza</div>
    <div>Oakmere, NC 27415</div>
  </div>
</section>

<section class="card card--back" aria-label="Business card back">
  <div class="back-pattern" role="img" aria-label="Repeating silver-foil gloss brand-symbol pattern across the card"></div>
  <div class="back-mark"></div>
</section>

</body>
</html>
```